Gather Every Thread Book Cover Design

We need:

Ebook and 6x 9 Inch trade paperback book cover (front, back, spine)

Book Title:Gather Every Thread
Subtitle: Getting Ready Before Hard Times Strike (Including Final Goodbyes) for Every Household

For a book written to help any of us gather the information needed to ensure we are set to take care of our loved ones in case of an emergency. Loved ones, a sense of urgency that leads to feeling calm and prepared is needed!

Target Market(s)

Any adult with children, a partner, parents or assets!

Industry/Entity Type

Financial Planning, Health care, Family

Font styles to use
Serif
Sans Serif

Colors
0054AA
0677BA
7BADD7
CADEEF
E8F1F8
FFF300
FFF600
FEFA6F
FFFEC7
FFFEE8
EE7325
F08F49
F5BC92
FAE3D3
FDF4ED
EB3D1F
EC4F4E
F09395
F8D3D4
FCEDEE

```html
<!DOCTYPE html>
<html lang="en">
<head>
<meta charset="utf-8">
<title>Gather Every Thread — Front Cover</title>
<link rel="stylesheet" href="https://fonts.googleapis.com/css2?family=Bebas+Neue&family=Oswald:wght@700&family=Questrial&display=swap">
<style>
  :root {
    --backdrop-light: #8a8a8a;
    --backdrop-dark: #4a4a4a;
    --cover-teal: #4cc3d7;
    --cover-teal-deep: #36b6cc;
    --title-white: #ffffff;
    --title-red: #e8141c;
    --ink: #1a1a1a;
    --accent-red: #eb1c24;
    --rule-white: #ffffff;
    --art-paper: #f3f8f9;
    --art-paper-shade: #cfe9ef;
    --art-shadow: #2a9fb5;
  }
  * { box-sizing: border-box; margin: 0; padding: 0; }
  html, body {
    width: 1200px; height: 1200px; overflow: hidden;
  }
  body {
    background: radial-gradient(circle at 50% 40%, var(--backdrop-light), var(--backdrop-dark));
    position: relative;
  }
  .front-cover {
    position: absolute;
    left: 240px; top: 60px;
    width: 720px; height: 1080px;
    background: linear-gradient(160deg, var(--cover-teal) 0%, var(--cover-teal-deep) 100%);
    box-shadow: 0 20px 50px rgba(0,0,0,0.35);
    overflow: hidden;
  }
  .title {
    position: absolute;
    left: 0; right: 0; top: 40px;
    text-align: center;
    font-family: "Bebas Neue", "Oswald", sans-serif;
    font-weight: 400;
    line-height: 0.86;
  }
  .title-lead {
    display: block;
    color: var(--title-white);
    font-size: 128px;
    letter-spacing: 1px;
  }
  .title-key {
    display: block;
    color: var(--title-red);
    font-size: 236px;
    letter-spacing: 4px;
  }
  .cover-art {
    position: absolute;
    left: 195px; top: 400px;
    width: 330px; height: 380px;
  }
  .subtitle {
    position: absolute;
    left: 50px; right: 50px; top: 800px;
    text-align: center;
    font-family: "Questrial", "Helvetica Neue", sans-serif;
    font-size: 29px;
    line-height: 1.25;
    color: var(--ink);
  }
  .subtitle-line { display: block; white-space: nowrap; }
  .subtitle-accent { color: var(--accent-red); }
  .cover-rule {
    position: absolute;
    left: 0; right: 0; top: 958px;
    height: 4px;
    background: var(--rule-white);
  }
  .author {
    position: absolute;
    left: 0; right: 0; top: 988px;
    text-align: center;
    font-family: "Oswald", "Bebas Neue", sans-serif;
    font-weight: 700;
    font-size: 40px;
    letter-spacing: 0.5px;
    color: var(--ink);
  }
</style>
</head>
<body>
  <main class="front-cover">
    <h1 class="title">
      <span class="title-lead">GATHER EVERY</span>
      <span class="title-key">THREAD</span>
    </h1>

    <svg class="cover-art" viewBox="0 0 330 380" role="img" aria-label="Illustration of a white paper-cut family of four holding hands beneath an umbrella topped with a red heart">
      <defs>
        <linearGradient id="artPaper" x1="0" y1="0" x2="1" y2="1">
          <stop offset="0%" stop-color="var(--art-paper)"/>
          <stop offset="100%" stop-color="var(--art-paper-shade)"/>
        </linearGradient>
        <filter id="artDrop" x="-20%" y="-20%" width="140%" height="140%">
          <feDropShadow dx="6" dy="10" stdDeviation="10" flood-color="var(--art-shadow)" flood-opacity="0.7"/>
        </filter>
      </defs>
      <rect x="15" y="10" width="300" height="350" rx="30" fill="url(#artPaper)" filter="url(#artDrop)"/>
    </svg>

    <p class="subtitle">
      <span class="subtitle-line">Getting Ready Before Hard Times Strike</span>
      <span class="subtitle-line"><span class="subtitle-accent">(Including Final Goodbyes)</span> for Every</span>
      <span class="subtitle-line">Household</span>
    </p>

    <div class="cover-rule"></div>

    <p class="author">MARINA HOLLOWAY</p>
  </main>
</body>
</html>
```